Jolly Paws Business Card Update

I have a business card which I love. I want to keep the same logo, colours, font and style. I want to upgrade the scripting and remove some elements and add others.
On the front side under Services - remove the existing wording and insert - Providing individual coaching strategies to create happy, healthy and social canine companions
Under Rebecca Thornley amend the current wording to read: Qualified in Dog Behavioural Training, Natural Animal Healthcare and Animal Health Science
On the reverse side to remove the web address.

```html
<!DOCTYPE html>
<html lang="en">
<head>
<meta charset="utf-8">
<title>Jolly Paws Business Card</title>
<link rel="stylesheet" href="https://fonts.googleapis.com/css2?family=Ubuntu:wght@500&family=Open+Sans:ital,wght@1,400&family=Arimo:wght@400;700&display=swap">
<style>
  :root {
    --page: #2a2a2a;
    --card-light: #f1f0ec;
    --ink-blue: #1c3f95;
    --name-blue: #1f5fb0;
    --brand-red: #c0171d;
    --brand-red-dark: #9e1016;
    --text-grey: #444444;
    --back-top: #1a3f9e;
    --back-bottom: #0a7fc7;
    --white: #ffffff;
  }
  html, body {
    margin: 0;
    padding: 0;
    width: 1138px;
    height: 1200px;
    overflow: hidden;
    background: var(--page);
  }
  .canvas {
    position: relative;
    width: 1138px;
    height: 1200px;
  }
  .card {
    position: absolute;
    width: 375px;
    height: 620px;
    border-radius: 14px;
    overflow: hidden;
  }
  .card-front {
    left: 156px;
    top: 276px;
    background: linear-gradient(180deg, #f4f3f0 0%, #ebe9e4 100%);
  }
  .card-back {
    left: 577px;
    top: 274px;
    background: linear-gradient(180deg, var(--back-top) 0%, var(--back-bottom) 100%);
  }
  .centered {
    position: absolute;
    left: 0;
    width: 100%;
    text-align: center;
    margin: 0;
  }
  .brand-mark {
    position: absolute;
    left: 0;
    width: 100%;
    display: flex;
    justify-content: center;
    align-items: center;
    gap: 10px;
    font-family: "Ubuntu", sans-serif;
    font-weight: 500;
  }
  .brand-dot {
    border-radius: 50%;
    background: var(--brand-red);
  }
  .front-brand {
    top: 86px;
    font-size: 30px;
    color: var(--ink-blue);
  }
  .front-brand .brand-dot { width: 22px; height: 22px; }
  .person-name {
    top: 198px;
    font-family: "Ubuntu", sans-serif;
    font-weight: 500;
    font-size: 25px;
    color: var(--name-blue);
  }
  .qualifications {
    top: 228px;
    font-family: "Open Sans", sans-serif;
    font-style: italic;
    font-size: 15px;
    line-height: 21px;
    color: var(--text-grey);
  }
  .contact-divider {
    position: absolute;
    top: 311px;
    left: 76px;
    width: 223px;
    height: 22px;
  }
  .contact-list {
    top: 345px;
    font-family: "Ubuntu", sans-serif;
    font-weight: 500;
    font-size: 16px;
    line-height: 23px;
    color: var(--text-grey);
    letter-spacing: 0.2px;
  }
  .services-band {
    position: absolute;
    left: 0;
    top: 455px;
    width: 100%;
    height: 89px;
    background: linear-gradient(180deg, #cf1d24 0%, var(--brand-red-dark) 100%);
  }
  .services-pill {
    position: absolute;
    left: 93px;
    top: 438px;
    width: 188px;
    height: 28px;
    border-radius: 14px;
    background: linear-gradient(180deg, #2a7fd0 0%, var(--ink-blue) 100%);
    border: 2px solid var(--white);
    box-sizing: border-box;
    color: var(--white);
    font-family: "Ubuntu", sans-serif;
    font-weight: 500;
    font-size: 18px;
    letter-spacing: 2.5px;
    text-align: center;
    line-height: 24px;
  }
  .services-text {
    top: 476px;
    font-family: "Arimo", sans-serif;
    font-size: 15px;
    line-height: 20px;
    color: var(--white);
  }
  .mission {
    top: 552px;
    font-family: "Arimo", sans-serif;
    font-size: 16px;
    line-height: 19px;
    color: var(--ink-blue);
  }
  .back-pattern {
    position: absolute;
    inset: 0;
    background: radial-gradient(circle at 50% 40%, rgba(255,255,255,0.06), rgba(255,255,255,0) 70%);
  }
  .back-brand {
    top: 500px;
    font-size: 40px;
    letter-spacing: 1px;
    color: var(--white);
  }
  .back-brand .brand-dot { width: 26px; height: 26px; }
  .tagline {
    top: 565px;
    font-family: "Arimo", sans-serif;
    font-size: 19px;
    color: var(--white);
    letter-spacing: 0.3px;
  }
</style>
</head>
<body>
<div class="canvas">

  <section class="card card-front">
    <div class="brand-mark front-brand"><span class="brand-dot"></span><span>Jolly Paws</span></div>

    <h1 class="centered person-name">Rebecca Thornley</h1>
    <p class="centered qualifications">Qualified in Dog Behavioural Training,<br>Natural Animal Healthcare and<br>Animal Health Science</p>

    <svg class="contact-divider" viewBox="0 0 223 22" aria-hidden="true">
      <line x1="0" y1="11" x2="78" y2="11" stroke="#c0171d" stroke-width="2"/>
      <line x1="145" y1="11" x2="223" y2="11" stroke="#c0171d" stroke-width="2"/>
      <g fill="#dfe8f5" stroke="#c0171d" stroke-width="1.6">
        <circle cx="88" cy="11" r="9.5"/>
        <circle cx="111.5" cy="11" r="9.5"/>
        <circle cx="135" cy="11" r="9.5"/>
      </g>
      <path d="M83.5 8.5c0-1.5 1-2.5 2-2.5l1 2.5-1.2 1c.5 1.3 1.5 2.3 2.8 2.8l1-1.2 2.5 1c0 1-1 2-2.5 2-3.2 0-5.6-2.4-5.6-5.6z" fill="#1c3f95"/>
      <rect x="106.5" y="7.5" width="10" height="7" rx="1" fill="#1c3f95"/>
      <path d="M106.5 8l5 3.5 5-3.5" fill="none" stroke="#fff" stroke-width="1"/>
      <g fill="none" stroke="#1c3f95" stroke-width="1">
        <circle cx="135" cy="11" r="5"/>
        <ellipse cx="135" cy="11" rx="2.2" ry="5"/>
        <line x1="130" y1="11" x2="140" y2="11"/>
      </g>
    </svg>

    <p class="centered contact-list">0412 555 019<br>jollypaws1@mail.com<br>www.jollypaws1.com</p>

    <div class="services-band"></div>
    <div class="services-pill">SERVICES</div>
    <p class="centered services-text">Providing Individual Coaching<br>Strategies to Create Happy,<br>Healthy and Social Canine Companions</p>

    <p class="centered mission">Promoting communication and<br>connection between dogs &amp; their families</p>
  </section>

  <section class="card card-back">
    <div class="back-pattern" role="img" aria-label="Faint repeating brand emblem pattern"></div>
    <div class="brand-mark back-brand"><span class="brand-dot"></span><span>JOLLY PAWS</span></div>
    <p class="centered tagline">HAPPY DOGS, HAPPY OWNERS</p>
  </section>

</div>
</body>
</html>
```